PURPLE LAGOON TENT

Hi

I need a tent, same style as before, but coordinating with our Purple Juniper Lagoon Color ,

I also need another patch. I would like it similar to this graphic ::
TRAIL MARSHAL definitely in yellow , i think it should be the yellow from our 2026 buck hunter patch , and maybe brown backing with it.

```html
<!DOCTYPE html>
<html lang="en">
<head>
<meta charset="utf-8">
<title>Purple Lagoon Tent</title>
<link rel="stylesheet" href="https://fonts.googleapis.com/css2?family=Arimo:wght@400;700&family=Montserrat:wght@500&display=swap">
<style>
  :root {
    --tent-purple: #4e2e8b;
    --brand-red: #e2262b;
    --seam-white: #ffffff;
    --page: #ffffff;
    --panel-seam: #6a4ea3;
    --patch-gold: #d2a22a;
    --patch-blue: #3a5ea6;
    --patch-blue-light: #5d80c2;
  }
  html, body {
    margin: 0;
    padding: 0;
    overflow: hidden;
    background: var(--page);
  }
  .sheet {
    position: relative;
    width: 789px;
    height: 1200px;
    overflow: hidden;
    background: var(--page);
  }
  .tent-shapes {
    position: absolute;
    inset: 0;
  }
  .brand-name {
    position: absolute;
    transform: translateX(-50%);
    font-family: "Arimo", Arial, sans-serif;
    font-weight: 700;
    color: var(--brand-red);
    white-space: nowrap;
    line-height: 1;
    letter-spacing: 1px;
  }
  .brand-name--large { font-size: 42px; }
  .brand-name--small { font-size: 16px; letter-spacing: 0.5px; }
  .brand-name--band { font-size: 12px; letter-spacing: 0.3px; }
  .band-tagline {
    position: absolute;
    transform: translateX(-50%);
    font-family: "Arimo", Arial, sans-serif;
    font-weight: 400;
    font-size: 14px;
    color: var(--seam-white);
    white-space: nowrap;
    line-height: 1;
  }
  .web-address {
    position: absolute;
    transform: translateX(-50%);
    font-family: "Montserrat", Arial, sans-serif;
    font-weight: 500;
    font-size: 8.5px;
    letter-spacing: 3.6px;
    color: var(--seam-white);
    white-space: nowrap;
    line-height: 1;
  }
  .patch {
    position: absolute;
    left: 431px;
    top: 874px;
    width: 290px;
    height: 290px;
    border-radius: 50%;
    box-sizing: border-box;
    border: 14px solid var(--patch-gold);
    background: radial-gradient(circle at 50% 40%, var(--patch-blue-light), var(--patch-blue) 75%);
    display: flex;
    flex-direction: column;
    align-items: center;
    justify-content: center;
  }
  .patch-name {
    font-family: "Arimo", Arial, sans-serif;
    font-weight: 700;
    font-size: 40px;
    line-height: 1.05;
    text-align: center;
    color: var(--patch-gold);
    margin-top: 40px;
  }
</style>
</head>
<body>
<main class="sheet">
  <svg class="tent-shapes" width="789" height="1200" viewBox="0 0 789 1200" aria-hidden="true">
    <g fill="var(--tent-purple)">
      <polygon points="215,46 386,247 43,247"/>
      <rect x="43" y="247" width="343" height="41"/>
      <polygon points="563,46 734,247 392,247"/>
      <rect x="392" y="247" width="342" height="41"/>
      <polygon points="208,306 379,507 36,507"/>
      <rect x="36" y="507" width="343" height="41"/>
      <polygon points="556,306 727,507 385,507"/>
      <rect x="385" y="507" width="342" height="41"/>
      <rect x="42" y="593" width="345" height="253"/>
      <rect x="399" y="593" width="345" height="253"/>
      <rect x="42" y="873" width="345" height="253"/>
    </g>
    <g stroke="var(--seam-white)" stroke-width="1">
      <line x1="43" y1="247.5" x2="386" y2="247.5"/>
      <line x1="392" y1="247.5" x2="734" y2="247.5"/>
      <line x1="36" y1="507.5" x2="379" y2="507.5"/>
      <line x1="385" y1="507.5" x2="727" y2="507.5"/>
    </g>
    <g stroke="var(--panel-seam)" stroke-width="0.8">
      <line x1="399" y1="708" x2="744" y2="708"/>
      <line x1="42" y1="988" x2="387" y2="988"/>
    </g>
  </svg>

  <!-- tent top 1 -->
  <div class="brand-name brand-name--large" style="left:215px; top:189px;">MARLO'S</div>
  <div class="brand-name brand-name--band" style="left:80px; top:265px;">MARLO'S</div>
  <div class="band-tagline" style="left:215px; top:264px;">ORGANIC TOPICAL RELIEF</div>
  <div class="brand-name brand-name--band" style="left:352px; top:265px;">MARLO'S</div>

  <!-- tent top 2 -->
  <div class="brand-name brand-name--large" style="left:563px; top:189px;">MARLO'S</div>
  <div class="brand-name brand-name--small" style="left:567px; top:268px;">MARLO'S</div>

  <!-- tent top 3 -->
  <div class="brand-name brand-name--large" style="left:208px; top:449px;">MARLO'S</div>
  <div class="brand-name brand-name--small" style="left:208px; top:528px;">MARLO'S</div>

  <!-- tent top 4 -->
  <div class="brand-name brand-name--large" style="left:556px; top:449px;">MARLO'S</div>
  <div class="brand-name brand-name--small" style="left:556px; top:528px;">MARLO'S</div>

  <!-- wall panel 1 -->
  <div class="brand-name brand-name--large" style="left:215px; top:649px;">MARLO'S</div>
  <div class="web-address" style="left:215px; top:700px;">www.MARLOSBOTANICS.com</div>

  <!-- wall panel 2 -->
  <div class="brand-name brand-name--large" style="left:572px; top:768px;">MARLO'S</div>
  <div class="web-address" style="left:572px; top:820px;">www.MARLOSBOTANICS.com</div>

  <!-- wall panel 3 -->
  <div class="brand-name brand-name--large" style="left:215px; top:1047px;">MARLO'S</div>
  <div class="web-address" style="left:215px; top:1099px;">www.MARLOSBOTANICS.com</div>

  <!-- patch -->
  <div class="patch" role="img" aria-label="Round patch with antler artwork and the name Trail Marshal">
    <div class="patch-name">TRAIL<br>MARSHAL</div>
  </div>
</main>
</body>
</html>
```